Redesign of business card for Silverbrook Mechanical

We are looking for a new design for our business cards for Silverbrook Mechanical. We are a plumbing & HVAC construction company, operating on the West Coast of Canada and USA. Logo attached.
Industry/Entity Type
Construction - Plumbing & HVAC
Contact Information for Business Card
Name, address, phone numbers, email, website address
Look and feel

```html
<!DOCTYPE html>
<html lang="en">
<head>
<meta charset="utf-8">
<title>Silverbrook Mechanical — Business Cards</title>
<link href="https://fonts.googleapis.com/css2?family=Oswald:wght@500&family=Lato:wght@400&display=swap" rel="stylesheet">
<style>
  :root {
    --backdrop: #8a8f8e;
    --paper: #ffffff;
    --ink: #111111;
    --ink-soft: #2a2a2a;
  }
  * { box-sizing: border-box; margin: 0; padding: 0; }
  html, body { width: 1200px; height: 828px; overflow: hidden; }
  body { background: var(--backdrop); position: relative; }

  .card {
    position: absolute;
    width: 472px;
    height: 270px;
    border-radius: 21px;
    overflow: hidden;
  }
  .card--light { background: var(--paper); color: var(--ink); }
  .card--dark { background: var(--ink); color: var(--paper); }
  .card--front.card--light { left: 112px; top: 130px; }
  .card--back.card--light  { left: 617px; top: 130px; }
  .card--front.card--dark  { left: 112px; top: 429px; }
  .card--back.card--dark   { left: 617px; top: 429px; }

  .brand {
    position: absolute;
    left: 0; right: 0;
    display: flex;
    align-items: center;
    justify-content: center;
    font-family: "Oswald", sans-serif;
    font-weight: 500;
    text-transform: uppercase;
    white-space: nowrap;
  }
  .brand__mark { background: currentColor; flex: none; }

  .card--front .brand { top: 58px; font-size: 17px; letter-spacing: 0.5px; gap: 9px; }
  .card--front .brand__mark { width: 15px; height: 15px; }

  .card--back .brand { top: 112px; font-size: 33px; letter-spacing: 0.8px; gap: 14px; }
  .card--back .brand__mark { width: 28px; height: 28px; }

  .person {
    position: absolute;
    right: 263px;
    top: 184px;
    text-align: right;
  }
  .person__name {
    font-family: "Oswald", sans-serif;
    font-weight: 500;
    font-size: 19px;
    line-height: 22px;
    letter-spacing: 0.3px;
    text-transform: uppercase;
  }
  .person__role {
    font-family: "Lato", sans-serif;
    font-size: 12.5px;
    line-height: 16px;
  }

  .divider {
    position: absolute;
    left: 227px;
    top: 167px;
    width: 1.5px;
    height: 78px;
    background: currentColor;
  }

  .contact {
    position: absolute;
    left: 244px;
    top: 163px;
    list-style: none;
    font-family: "Lato", sans-serif;
    font-size: 12.5px;
    line-height: 16.6px;
  }
  .contact li { display: flex; align-items: center; white-space: nowrap; }
  .contact .icon { width: 10px; height: 10px; margin-right: 8px; flex: none; fill: currentColor; }
</style>
</head>
<body>

  <section class="card card--light card--front">
    <div class="brand"><span class="brand__mark"></span><span>Silverbrook Mechanical</span></div>
    <div class="person">
      <p class="person__name">Daniel Reyes</p>
      <p class="person__role">Founder and CEO</p>
    </div>
    <div class="divider"></div>
    <ul class="contact">
      <li>4127 Harbor Point Road</li>
      <li>Suite 210, Tacoma, WA 98402</li>
      <li><svg class="icon" viewBox="0 0 10 10"><path d="M1 3.5 Q5 0.5 9 3.5 L8 5 L6.5 4 V3.2 H3.5 V4 L2 5 Z M2.5 5.5 H7.5 L8.5 9 H1.5 Z"/></svg>253-555-0148</li>
      <li><svg class="icon" viewBox="0 0 10 10"><path d="M0.5 2 H9.5 V2.8 L5 5.8 L0.5 2.8 Z M0.5 3.8 L5 6.8 L9.5 3.8 V8.5 H0.5 Z"/></svg>Reyes@silverbrookmech.com</li>
      <li><svg class="icon" viewBox="0 0 10 10"><circle cx="5" cy="5" r="4.2" fill="none" stroke="currentColor" stroke-width="0.9"/><ellipse cx="5" cy="5" rx="1.8" ry="4.2" fill="none" stroke="currentColor" stroke-width="0.8"/><path d="M0.8 5 H9.2" stroke="currentColor" stroke-width="0.8"/></svg>www.silverbrookmech.com</li>
    </ul>
  </section>

  <section class="card card--light card--back">
    <div class="brand"><span class="brand__mark"></span><span>Silverbrook Mechanical</span></div>
  </section>

  <section class="card card--dark card--front">
    <div class="brand"><span class="brand__mark"></span><span>Silverbrook Mechanical</span></div>
    <div class="person">
      <p class="person__name">Daniel Reyes</p>
      <p class="person__role">Founder and CEO</p>
    </div>
    <div class="divider"></div>
    <ul class="contact">
      <li>4127 Harbor Point Road</li>
      <li>Suite 210, Tacoma, WA 98402</li>
      <li><svg class="icon" viewBox="0 0 10 10"><path d="M1 3.5 Q5 0.5 9 3.5 L8 5 L6.5 4 V3.2 H3.5 V4 L2 5 Z M2.5 5.5 H7.5 L8.5 9 H1.5 Z"/></svg>253-555-0148</li>
      <li><svg class="icon" viewBox="0 0 10 10"><path d="M0.5 2 H9.5 V2.8 L5 5.8 L0.5 2.8 Z M0.5 3.8 L5 6.8 L9.5 3.8 V8.5 H0.5 Z"/></svg>Reyes@silverbrookmech.com</li>
      <li><svg class="icon" viewBox="0 0 10 10"><circle cx="5" cy="5" r="4.2" fill="none" stroke="currentColor" stroke-width="0.9"/><ellipse cx="5" cy="5" rx="1.8" ry="4.2" fill="none" stroke="currentColor" stroke-width="0.8"/><path d="M0.8 5 H9.2" stroke="currentColor" stroke-width="0.8"/></svg>www.silverbrookmech.com</li>
    </ul>
  </section>

  <section class="card card--dark card--back">
    <div class="brand"><span class="brand__mark"></span><span>Silverbrook Mechanical</span></div>
  </section>

</body>
</html>
```